Design business cards for Ironvale Barbers (Opening March so won't need finalised till January2018

Ironvale Barbers is the new age barbers and skincare for all men. Creating tailor made haircuts & customised skincare solutions for the perfect healthy manly look. The Barbers will have a industrial, rustic, worldly feel about it. Rustic red brick wall with old wine barrels as the work stations with the old fashion barber chairs. Concrete floor and a bit corrugated iron around.
Target Market(s)
Professional males who like a great haircut, wet shave and may consider a facial if in the right environment. Total pampering experience in a boys environment.
Industry/Entity Type
Barber
Contact Information for Business Card
Front- Logo - address is 42 Kowhai Rd Taupo
Ph - (07) 548 9163
www.ironvalebarbers.com
email - hello@ironvale.co.nz
Back of card
Mens Haircare - Wet Shaving - Facials - Skin Prescriptions
We are doing a loyalty program - 6 squares numbered then 7th free
Colors
Designer to choose colors to be used in the design.
Requirements
Must have
- Clean simple easy to read.
Nice to have
- Our current colours are white font on black background but thinking we need to introduce another colour. Maybe white logo on a copper, bronze or rusty background. Or even a rustic red brick wall with white writing. Want it clean simple to read. Maybe a burgundy?
Should not have
- no images like heads, scissors, razors please

```html
<!DOCTYPE html>
<html lang="en">
<head>
<meta charset="utf-8">
<title>Ironvale Barbers – Business Cards</title>
<link href="https://fonts.googleapis.com/css2?family=Lato:wght@400;700;900&display=swap" rel="stylesheet">
<style>
  :root {
    --stage: #758889;
    --card-dark: #1a1a1a;
    --card-light: #ffffff;
    --ink-light: #ffffff;
    --ink-dark: #2e3133;
    --rule-dark: #3a3d3f;
    --shadow: rgba(30, 45, 46, 0.35);
  }
  html, body {
    margin: 0;
    padding: 0;
    width: 1200px;
    height: 1200px;
    overflow: hidden;
    background: var(--stage);
    font-family: "Lato", sans-serif;
  }
  .stage { position: relative; width: 1200px; height: 1200px; }
  .card {
    position: absolute;
    left: 293px;
    width: 615px;
    height: 351px;
    border-radius: 32px;
    box-shadow: 0 10px 18px -8px var(--shadow);
  }
  .card-front { top: 190px; background: var(--card-dark); color: var(--ink-light); }
  .card-back { top: 661px; background: var(--card-light); color: var(--ink-dark); }

  .brand-name {
    position: absolute;
    left: 0; right: 0;
    top: 72px;
    text-align: center;
    font-weight: 900;
    line-height: 1;
    text-transform: uppercase;
  }
  .brand-name .brand-main { display: block; font-size: 50px; letter-spacing: 1px; }
  .brand-name .brand-sub { display: block; font-size: 20px; letter-spacing: 7px; margin-top: 8px; }

  .holder {
    position: absolute;
    right: calc(615px - 289px);
    top: 210px;
    text-align: right;
  }
  .holder-name { font-size: 20px; font-weight: 700; letter-spacing: 0.3px; line-height: 1; }
  .holder-role { font-size: 14.5px; margin-top: 4px; line-height: 1; }

  .divider {
    position: absolute;
    left: 304px; top: 195px;
    width: 2px; height: 88px;
    background: var(--ink-light);
  }
  .contact-list {
    position: absolute;
    left: 321px; top: 200px;
    margin: 0; padding: 0;
    list-style: none;
    font-size: 12.2px;
  }
  .contact-list li { display: flex; align-items: center; height: 20px; }
  .contact-list svg { width: 8px; height: 8px; margin-right: 12px; fill: var(--ink-light); flex: none; }

  .services {
    position: absolute;
    left: 88px; top: 140px;
    margin: 0; padding: 0;
    list-style: none;
    font-size: 18.5px;
    line-height: 22px;
  }
  .booking { position: absolute; left: 296px; top: 154px; font-size: 18.5px; }
  .booking-row { display: flex; align-items: flex-end; height: 22px; }
  .booking-row + .booking-row { margin-top: 22px; }
  .booking-field { display: inline-block; border-bottom: 1.5px solid var(--ink-dark); margin-left: 6px; height: 16px; }
  .field-date { width: 158px; }
  .field-time { width: 185px; }
</style>
</head>
<body>
<div class="stage">

  <section class="card card-front" aria-label="Card front">
    <div class="brand-name">
      <span class="brand-main">Ironvale</span>
      <span class="brand-sub">Barbers</span>
    </div>

    <div class="holder">
      <div class="holder-name">YOUR NAME</div>
      <div class="holder-role">Designation</div>
    </div>

    <div class="divider"></div>

    <ul class="contact-list">
      <li><svg viewBox="0 0 10 10"><path d="M2 0.5 L3.6 0.5 L4.2 2.8 L3 3.6 C3.6 5 4.9 6.4 6.4 7 L7.2 5.8 L9.5 6.4 L9.5 8 C9.5 9 8.6 9.6 7.6 9.4 C4.2 8.7 1.3 5.8 0.6 2.4 C0.4 1.4 1 0.5 2 0.5Z"/></svg>(07) 548 9163</li>
      <li><svg viewBox="0 0 10 10"><path d="M5 0.5 A4.5 4.5 0 1 0 8.5 7.8 L7.6 7.1 A3.3 3.3 0 1 1 8.3 5 L8.3 5.6 C8.3 6.3 7.3 6.3 7.3 5.6 L7.3 3 L6.3 3 L6.3 3.4 A2.2 2.2 0 1 0 6.6 6.5 C7.3 7.7 9.5 7.3 9.5 5.6 L9.5 5 A4.5 4.5 0 0 0 5 0.5Z M5 3.9 A1.1 1.1 0 1 1 5 6.1 A1.1 1.1 0 1 1 5 3.9Z"/></svg>hello@ironvale.co.nz</li>
      <li><svg viewBox="0 0 10 10"><path d="M5 0.3 A3.4 3.4 0 0 0 1.6 3.7 C1.6 6.2 5 9.7 5 9.7 C5 9.7 8.4 6.2 8.4 3.7 A3.4 3.4 0 0 0 5 0.3Z M5 2.4 A1.3 1.3 0 1 1 5 5 A1.3 1.3 0 1 1 5 2.4Z"/></svg>42 Kowhai Rd Taupo</li>
      <li><svg viewBox="0 0 10 10"><path d="M6.2 0.8 L9.2 3.8 L7.2 5.8 L6.4 5 L7.8 3.8 L6.2 2.2 L4.8 3.6 L4 2.8Z M3.8 9.2 L0.8 6.2 L2.8 4.2 L3.6 5 L2.2 6.2 L3.8 7.8 L5.2 6.4 L6 7.2Z M3.3 6.1 L6.1 3.3 L6.7 3.9 L3.9 6.7Z"/></svg>www.ironvalebarbers.com</li>
    </ul>
  </section>

  <section class="card card-back" aria-label="Card back">
    <ul class="services">
      <li>Mens Haircare</li>
      <li>Wet Shaving</li>
      <li>Facials</li>
      <li>Skin Prescriptions</li>
    </ul>

    <div class="booking">
      <div class="booking-row">Date -<span class="booking-field field-date"></span></div>
      <div class="booking-row">Time -<span class="booking-field field-time"></span></div>
    </div>
  </section>

</div>
</body>
</html>
```